Company director needs a business card design

I am a semi-retired former senior finance executive who sits on a number of public and private company boards and do some consulting work. I work largely with emerging businesses but deal regularly with top end of town lawyers, bankers etc. I need a thoughtful but relatively conservative design which would also resonate with my younger client base. Some colour would be good. Information limited to name, address, office tel, mobile and email.

Industry/Entity Type

Finance

```html
<!DOCTYPE html>
<html lang="en">
<head>
<meta charset="utf-8">
<title>Martin Calloway – Business Card</title>
<link rel="stylesheet" href="https://fonts.googleapis.com/css2?family=Lora:wght@400;700&display=swap">
<style>
  :root {
    --backdrop: #8a9dcf;
    --card: #ffffff;
    --brand-blue: #2d63b8;
    --soft-blue: #6f87cf;
    --pale-blue: #c9d3ee;
    --ink: #1e1e24;
    --ink-soft: #3a3a44;
  }
  * { box-sizing: border-box; margin: 0; padding: 0; }
  html, body {
    width: 1200px;
    height: 900px;
    overflow: hidden;
    background: var(--backdrop);
    font-family: "Lora", Georgia, serif;
  }
  .canvas {
    width: 1200px;
    height: 900px;
    display: flex;
    align-items: center;
    justify-content: center;
    gap: 40px;
  }
  .card {
    position: relative;
    width: 560px;
    height: 342px;
    background: var(--card);
    overflow: hidden;
    box-shadow: 0 10px 30px rgba(30, 40, 90, 0.25);
  }
  .card__pattern--front {
    position: absolute;
    top: 0;
    right: 0;
    width: 58%;
    height: 100%;
    background: linear-gradient(to left, var(--brand-blue) 0%, var(--soft-blue) 45%, var(--pale-blue) 75%, rgba(255,255,255,0) 100%);
  }
  .card__pattern--back {
    position: absolute;
    inset: 0;
    background: linear-gradient(135deg, var(--soft-blue) 0%, var(--brand-blue) 55%, var(--soft-blue) 100%);
  }
  .identity {
    position: absolute;
    left: 44px;
    top: 96px;
  }
  .identity__name {
    font-size: 27px;
    letter-spacing: 0.5px;
    line-height: 1;
    white-space: nowrap;
  }
  .identity__first {
    color: var(--brand-blue);
    font-weight: 700;
  }
  .identity__last {
    color: var(--ink);
    font-weight: 400;
  }
  .contacts {
    list-style: none;
    margin-top: 42px;
    margin-left: 60px;
  }
  .contacts__item {
    display: flex;
    align-items: center;
    gap: 12px;
    font-size: 13px;
    color: var(--ink-soft);
    line-height: 1;
    margin-bottom: 11px;
    white-space: nowrap;
  }
  .contacts__icon {
    width: 12px;
    height: 12px;
    flex: none;
    fill: var(--brand-blue);
  }
</style>
</head>
<body>
<main class="canvas">
  <section class="card card--front">
    <div class="card__pattern--front" role="img" aria-label="Decorative pattern of blue rounded squares fading towards the left"></div>
    <div class="identity">
      <h1 class="identity__name"><span class="identity__first">MARTIN</span> <span class="identity__last">CALLOWAY</span></h1>
      <ul class="contacts">
        <li class="contacts__item">
          <svg class="contacts__icon" viewBox="0 0 12 12" aria-hidden="true"><path d="M2.5 0.8 L4.4 2.9 L3.4 4.2 C4 5.8 5.7 7.7 7.8 8.6 L9 7.6 L11.2 9.5 L9.8 11.2 C5.5 11 1 6.6 0.8 2.2 Z"/></svg>
          <span>02 9000 1482</span>
        </li>
        <li class="contacts__item">
          <svg class="contacts__icon" viewBox="0 0 12 12" aria-hidden="true"><path d="M3 0.5 H9 V11.5 H3 Z M4 1.8 V9 H8 V1.8 Z"/><circle cx="6" cy="10.2" r="0.6"/></svg>
          <span>0400 318 275</span>
        </li>
        <li class="contacts__item">
          <svg class="contacts__icon" viewBox="0 0 12 12" aria-hidden="true"><path d="M0.5 2 H11.5 V10 H0.5 Z M1.5 3.2 V9 H10.5 V3.2 L6 6.6 Z"/></svg>
          <span>martin_calloway@example.net.au</span>
        </li>
        <li class="contacts__item">
          <svg class="contacts__icon" viewBox="0 0 12 12" aria-hidden="true"><path d="M6 0.8 L11.5 6 H9.8 V11.2 H7.2 V7.8 H4.8 V11.2 H2.2 V6 H0.5 Z"/></svg>
          <span>18 Kestrel avenue, Harbourside NSW 2000</span>
        </li>
      </ul>
    </div>
  </section>
  <section class="card card--back">
    <div class="card__pattern--back" role="img" aria-label="All-over decorative pattern of blue rounded squares"></div>
  </section>
</main>
</body>
</html>
```